Web Page for Elearning project

SUMMARY OF REQUIREMENT
The requirement is to provide the graphic design for an eLearning project. I need the design elements for a main page layout which I can recreate in an eLearning authoring program (Lectora) using the graphic design you provide.

SUMMARY OF SITE PAGES
The web site has 11 sections with pages within each section. The user will navigate through all pages by clicking NEXT or by jumping to a page using either an index or table of contents (according to your design).

The sections are:
- Introduction
- TWP Cemeteries
- Ashvale*
- Meadow of Pines (Catholic)*
- Tallow Bend (Catholic)*
- Dunmarrow (Catholic)*
- Wyatts Hollow (Catholic)*
- Meadow of Pines (Presbyterian)*
- Brenta Vale*
- Summary
- Quiz

The sections with a "*" contain consistent pages - which I imagine could be accessed by clicking on a tab or button. I would need you to supply the graphics to be able to set them up in my elearning program. The pages are:
- History
- Map
- Contact
- Directions
- Services
- Sections

ONCE THE DESIGN IS ACCEPTED...
Ultimately I need the background graphics so I can implement the design in my elearning authoring program What else do you need to know?

SEE ATTACHED PDF FOR MORE DETAILS AND EXAMPLES OF WHAT I AM CURRENTLY WORKING WITH

Reason: Project was set up incorrectly for the first 6 days of the job

Reason: Australia now has public holidays for the next 5 days.  Everyone back at work on 27-28 April.

Target Market(s)

The users are mostly middle-aged women who only have basic computer skills... needs to be easy to navigate.

Industry/Entity Type

Graphic Design

Requirements
Must have
• Light, fun but professional. Its training...should have a light/easy feel about it.

Must be easy to look at. The design should support the overall navigation/structure.
Nice to have
• easy to look at, light.
Should not have
• Should not use serif fonts.
I don't think we'd go for bold lime green or any really zany colours.

```html
<!DOCTYPE html>
<html lang="en">
<head>
<meta charset="utf-8">
<title>Meadow of Pines – History</title>
<link href="https://fonts.googleapis.com/css2?family=Didact+Gothic&family=Poppins:wght@600&display=swap" rel="stylesheet">
<style>
:root{
  --sky:#0aa1e2;
  --navy:#0a5f8c;
  --pill:#0b6fa7;
  --ink:#1a1a1a;
  --muted:#a6a6a6;
  --line:#d9d9d9;
  --white:#ffffff;
  --helper:#1a9ad6;
}
*{box-sizing:border-box;margin:0;padding:0}
html,body{width:1200px;height:854px;overflow:hidden;background:var(--white)}
body{font-family:"Didact Gothic",sans-serif;color:var(--ink);position:relative}

.toolbar{position:absolute;left:0;top:0;width:1200px;height:124px;
  background:linear-gradient(#ffffff 0%,#f6f6f6 70%,#e6e6e6 100%);
  border-bottom:1px solid #cfcfcf;display:flex}
.brand{width:136px;height:124px;display:flex;align-items:center;justify-content:center;gap:6px;
  border-right:1px solid var(--line);font-size:14px;color:var(--navy)}
.brand .dot{width:10px;height:10px;border-radius:50%;background:var(--navy)}
.tool{display:flex;flex-direction:column;align-items:center;justify-content:center;gap:10px;
  border-right:1px solid var(--line);color:var(--muted);font-size:23px;letter-spacing:.3px}
.tool svg{width:30px;height:30px;fill:var(--muted)}
.close-wrap{flex:1;display:flex;align-items:center;justify-content:center}
.close{width:121px;height:43px;border-radius:22px;background:linear-gradient(#f2f2f2,#d6d6d6);
  box-shadow:0 1px 2px rgba(0,0,0,.25);display:flex;align-items:center;justify-content:center;
  font-size:18px;color:#666}

.banner{position:absolute;left:0;top:124px;width:1200px;height:105px;background:var(--sky)}
.banner h1{position:absolute;left:32px;top:22px;font-family:"Poppins",sans-serif;font-weight:600;
  font-size:50px;color:var(--white);letter-spacing:-.5px}
.toc-label{position:absolute;left:738px;top:43px;font-size:16px;color:var(--white);font-weight:bold;letter-spacing:.2px}
.toc-select{position:absolute;left:917px;top:27px;width:254px;height:49px;border-radius:25px;
  background:var(--pill);color:var(--white);font-size:22px;padding:10px 22px;box-shadow:0 1px 3px rgba(0,0,0,.3)}
.toc-select svg{position:absolute;right:24px;top:20px}

.photo{position:absolute;left:27px;width:290px;height:220px;background:var(--white);
  padding:7px;border-radius:4px;box-shadow:0 1px 6px rgba(0,0,0,.35)}
.photo .fill{width:100%;height:100%}
.photo-a{top:256px}.photo-a .fill{background:linear-gradient(#d8dde0 0%,#7d8a6a 45%,#5e7a3c 100%)}
.photo-b{top:501px}.photo-b .fill{background:linear-gradient(#cfd6da 0%,#5a6b4c 40%,#4a3f40 100%)}

.article{position:absolute;left:355px;top:253px;width:520px}
.article h2{font-family:"Poppins",sans-serif;font-weight:600;font-size:35px;letter-spacing:-.5px}
.article .body{margin-top:16px;height:400px;overflow:hidden;font-size:16.5px;line-height:25px}
.article p+p{margin-top:25px}

.scroll{position:absolute;left:893px;top:285px;width:25px;height:432px}
.scroll .track{position:absolute;left:0;top:22px;width:25px;height:388px;border:1px solid #cfcfcf;border-radius:13px}
.scroll .thumb{position:absolute;left:3px;top:64px;width:17px;height:266px;background:#d2d2d2;border-radius:9px}
.scroll .arrow{position:absolute;left:7px;color:#999;font-size:13px}

.bubble{position:absolute;left:952px;top:260px;width:211px;height:208px;background:var(--white);
  border:1px solid #dcdcdc;border-radius:12px;box-shadow:0 1px 4px rgba(0,0,0,.15);padding:18px 18px}
.bubble h3{font-size:16px;color:var(--helper);font-weight:bold}
.bubble p{margin-top:10px;font-size:14.5px;line-height:20.5px;color:#222}
.bubble .tail{position:absolute;left:30px;bottom:-29px}
.helper{position:absolute;left:977px;top:513px;width:223px;height:247px;
  background:linear-gradient(#ffffff 0%,#eef4f8 100%)}

.tabs{position:absolute;left:0;top:770px;width:1200px;height:84px;background:var(--navy)}
.tab{position:absolute;top:0;height:76px;line-height:78px;font-size:26px;color:var(--white);
  text-align:center;transform:translateX(-50%)}
.tab.active{background:var(--white);color:var(--ink);width:141px;left:222px}
</style>
</head>
<body>

<header class="toolbar">
  <div class="brand"><span class="dot"></span>TWP Cemeteries</div>
  <div class="tool" style="width:120px">
    <svg viewBox="0 0 30 30"><path d="M15 4 3 15h4v11h6v-7h4v7h6V15h4z"/></svg>HOME</div>
  <div class="tool" style="width:94px">
    <svg viewBox="0 0 30 30"><path d="M19 6 9 15l10 9" fill="none" stroke="#a6a6a6" stroke-width="3"/></svg>BACK</div>
  <div class="tool" style="width:109px">
    <svg viewBox="0 0 30 30"><path d="M11 6l10 9-10 9" fill="none" stroke="#a6a6a6" stroke-width="3"/></svg>NEXT</div>
  <div class="tool" style="width:148px">
    <svg viewBox="0 0 30 30"><rect x="12" y="5" width="7" height="6"/><rect x="2" y="19" width="7" height="6"/><rect x="12" y="19" width="7" height="6"/><rect x="22" y="19" width="7" height="6"/><path d="M15 11v8M5 19v-4h21v4" fill="none" stroke="#a6a6a6" stroke-width="2"/></svg>SITE MAP</div>
  <div class="tool" style="width:107px">
    <svg viewBox="0 0 30 30"><rect x="8" y="9" width="14" height="19" rx="7"/><path d="M15 9V5c0-2 3-2 3-4" fill="none" stroke="#a6a6a6" stroke-width="2"/></svg>LINKS</div>
  <div class="tool" style="width:114px">
    <svg viewBox="0 0 30 30"><text x="15" y="25" text-anchor="middle" font-size="26" font-family="sans-serif" fill="#a6a6a6">?</text></svg>HELP</div>
  <div class="tool" style="width:172px">
    <svg viewBox="0 0 30 30"><path d="M7 3h11l6 6v18H7z"/><path d="M10 14h11M10 18h11M10 22h11" stroke="#fff" stroke-width="1.5"/></svg>RESOURCES</div>
  <div class="close-wrap"><div class="close">X CLOSE</div></div>
</header>

<section class="banner">
  <h1>Meadow of Pines</h1>
  <span class="toc-label">TABLE OF CONTENTS</span>
  <div class="toc-select">Meadow of Pines
    <svg width="16" height="10" viewBox="0 0 16 10"><path d="M0 0h16L8 10z" fill="#fff"/></svg>
  </div>
</section>

<figure class="photo photo-a"><div class="fill" role="img" aria-label="Photo of old headstones among palm trees in the cemetery"></div></figure>
<figure class="photo photo-b"><div class="fill" role="img" aria-label="Photo of polished granite memorials with flowers"></div></figure>

<article class="article">
  <h2>History</h2>
  <div class="body">
    <p>The Meadow of Pines Cemetery was officially opened in 1890 to serve the inner-western suburbs such as Harrowgate and Kellbrook as well as Ferncliff. The first burial was a Roman Catholic, Eliza Jane Moore, on the 3rd September, 1890.</p>
    <p>The Meadow of Pines Cemetery was required because the grave-yards at St Brigid's Anglican Church, St Linus Catholic Church and a Baptist Community Cemetery at Ferncliff were becoming overcrowded and the population in the Ferncliff area was growing. Thus, in 1887 Ferncliff Council claimed 11 hectares of land from the Meadow of Pines Common to form the Meadow of Pines Cemetery. Over-crowding became so serious at St Brigid's Cemetery that in 1891 the council ordered that no more burials would be permitted there after the last day of the century. Council feared '...the soak-age from St Brigid's was infecting neighbouring wells and would cause an epidemic of fever.'</p>
  </div>
</article>

<div class="scroll">
  <span class="arrow" style="top:0">^</span>
  <div class="track"><div class="thumb"></div></div>
  <span class="arrow" style="top:414px">v</span>
</div>

<aside class="bubble">
  <h3>Hi, I'm Mr. Helper Guy</h3>
  <p>Lorem ipsum dolor sit amet, consectetur adipisicing elit, sed do eiusmod tempor incid-idunt ut labore et dolore magna aliqua.</p>
  <svg class="tail" width="24" height="30" viewBox="0 0 24 30"><path d="M0 0h24L6 30z" fill="#fff"/><path d="M0 1 6 30 24 1" fill="none" stroke="#dcdcdc"/></svg>
</aside>
<div class="helper" role="img" aria-label="Cartoon helper character in shirt and tie leaning on a box"></div>

<nav class="tabs">
  <span class="tab" style="left:72px">Quiz</span>
  <span class="tab active">History</span>
  <span class="tab" style="left:371px">Maps</span>
  <span class="tab" style="left:548px">Directions</span>
  <span class="tab" style="left:738px">Services</span>
  <span class="tab" style="left:920px">Sections</span>
  <span class="tab" style="left:1106px">Contact</span>
</nav>

</body>
</html>
```